Redesign of our homepage

We are a company that operates in the Wellness tourism sector. We are starting a project to redesign our homepage. See the screenshots. The main idea is that the banner image and the text on the banner are dynamically replaced depending on whether a user clicks on the "Thumb up" or the "Thumb down" icon.
You can see a live version of our homepage at http://demo.verdalumo.com

Industry/Entity Type

Health And Wellness

Coding

Coded - Design and coding required

Number of Pages Required

1 page

Requirements
Must have
• Must abide by style and look & feel of the current site.
It is important to demonstrate the functionality that enables the banner image and text being refreshed at each click of a ThumbUp or ThumbDown icons. In others words the Javascript must work.

Let me add some more context on the project.

Actually the thumb up and thumb down are possible answers to question/comment dynamically displayed at the location of the current text "Experience That Make You tell an unforgettable story".
An example of a comment/question is "I need a program that would help limit my stress levels and make me look great and feel fantastic". Or "I need an activity that will reduce my stress."
So a user would have to click on a thumb up or thumb down to approve or disapprove these questions/comments..
Based on this information, I think you could move the thumbs up to the left and right side of the text (the comment/question) respectively. And move the reset underneath in the middle.

Maybe it's a good idea to reduce the font size of that text as well.

And now to the dropdown list. We need only 2 of them, and not 3 as you have displayed.
One of them contain the list:
-- I need a weekend retreat
-- ! need a week or more retreat
The other would contain a list of countries.
The drop down values must be selected before the thumbs up and down thumbs are active.
Therefore you should move them above the question/comment text.
And finally about the thumbs and reset icons. Please put them in a round orange color and make them a bit bigger.

```html
<!DOCTYPE html>
<html lang="en">
<head>
<meta charset="utf-8">
<title>verdalumo — homepage concepts</title>
<link href="https://fonts.googleapis.com/css2?family=Lato:wght@400;700&family=Oswald:wght@300;700&display=swap" rel="stylesheet">
<style>
:root{
  --orange:#f0922b;
  --orange-deep:#d97a17;
  --ink:#1e1e1e;
  --white:#ffffff;
  --mist:#e9e9e9;
  --pill:#e6e6e6;
  --pill-text:#555;
  --grey-btn:#8a8f92;
  --divider:#ffffff;
}
*{box-sizing:border-box;margin:0;padding:0}
html,body{width:1200px;height:1200px;overflow:hidden;background:var(--divider)}
body{position:relative;font-family:"Lato",sans-serif;color:var(--ink)}

.concept{position:absolute;top:0;width:593px;height:1200px;overflow:hidden;background:var(--mist)}
.concept--adventure{left:0}
.concept--wild{left:607px}

.hero-photo{position:absolute;inset:0 0 auto 0;height:480px}
.concept--adventure .hero-photo{
  background:linear-gradient(180deg,#7fa3ad 0%,#9db7bb 18%,#5f7283 32%,#3f4e5f 48%,#6b7a88 62%,#dfe2e4 84%,var(--mist) 100%);
}
.concept--wild .hero-photo{
  height:560px;
  background:
   radial-gradient(ellipse 120px 190px at 240px 250px,#5a3a26 0%,#4a2f1f 60%,transparent 100%),
   linear-gradient(180deg,#f4f2ee 0%,#9a8b68 14%,#6f6a4d 28%,#b49a72 48%,#d9c7a6 66%,#ebe4d8 84%,var(--mist) 100%);
}
.forest-photo{position:absolute;left:0;right:0;bottom:0;height:170px;
  background:linear-gradient(180deg,var(--mist) 0%,#9aa1a4 22%,#4f5a5d 55%,#2b3434 100%)}
.concept--wild .forest-photo{background:linear-gradient(180deg,var(--mist) 0%,#a09f98 22%,#555a55 55%,#2e322e 100%)}

/* header */
.site-header{position:absolute;top:22px;left:0;right:0;height:20px}
.brand{position:absolute;left:84px;top:0;display:flex;align-items:center;gap:4px;
  font-family:"Lato",sans-serif;font-size:13px;color:var(--orange);letter-spacing:.3px}
.brand-dot{width:9px;height:9px;border-radius:50%;background:#6b6b6b}
.main-nav{position:absolute;left:239px;top:4px;display:flex;gap:14px;font-size:7px;font-weight:700;color:var(--ink);letter-spacing:.3px}
.main-nav .currency::after{content:" ▾"}
.sign-in{position:absolute;left:460px;top:3px;width:46px;height:12px;border-radius:6px;background:var(--orange);
  color:var(--white);font-size:6.5px;font-weight:700;text-align:center;line-height:12px}

/* filters */
.filter{position:absolute;height:16px;border-radius:8px;background:var(--pill);display:flex;align-items:center;
  padding:0 7px;font-size:5.5px;color:var(--pill-text);gap:5px}
.filter .chev{margin-left:auto;font-size:6px}
.filter-dot{width:8px;height:8px;border-radius:50%;border:1px solid #777}
.filter--retreat{left:163px;width:112px}
.filter--country{left:300px;width:130px}
.concept--adventure .filter{top:78px}
.concept--wild .filter{top:158px}
.sort-by{position:absolute;left:389px;width:103px;height:16px;border-radius:8px;background:#f1f1f1;display:flex;align-items:center;padding:0 7px;gap:5px;font-size:5.5px;color:var(--pill-text)}
.sort-by .funnel{width:0;height:0;border-left:4px solid transparent;border-right:4px solid transparent;border-top:6px solid #555}
.sort-by .chev{margin-left:auto;font-size:6px}
.concept--adventure .sort-by{top:448px}
.concept--wild .sort-by{top:462px}

/* social */
.social{position:absolute;display:flex;flex-direction:column;gap:12px}
.social span{width:6px;height:6px;border-radius:50%;background:var(--white)}
.concept--adventure .social{left:114px;top:156px}
.concept--wild .social{left:113px;top:121px}

/* headline */
.headline{position:absolute;font-family:"Oswald",sans-serif;color:var(--white)}
.headline .lead{display:block;font-weight:300;font-size:20px;line-height:20px}
.headline .big{display:block;font-weight:700;line-height:1}
.concept--adventure .headline{left:143px;top:110px}
.concept--adventure .headline .lead{font-style:italic}
.concept--adventure .headline .big{font-size:50px;margin:-6px 0 0 98px;letter-spacing:1px}
.concept--wild .headline{left:356px;top:194px}
.concept--wild .headline .lead{font-size:19px}
.concept--wild .headline .big{font-size:50px;margin-top:0;letter-spacing:1px}

/* vote controls */
.vote{position:absolute;border-radius:50%;display:flex;align-items:center;justify-content:center;box-shadow:0 2px 4px rgba(0,0,0,.25)}
.vote--up,.vote--down{background:var(--orange)}
.vote--reset{background:var(--grey-btn)}
.concept--adventure .vote{width:38px;height:38px;top:185px}
.concept--adventure .vote--up{left:180px}
.concept--adventure .vote--reset{left:278px}
.concept--adventure .vote--down{left:376px}
.concept--wild .vote{width:24px;height:24px;top:272px}
.concept--wild .vote--up{left:344px}
.concept--wild .vote--reset{left:406px}
.concept--wild .vote--down{left:467px}
.vote svg{width:55%;height:55%}

.scroll-cue{position:absolute;width:12px;height:14px}
.concept--adventure .scroll-cue{left:291px;top:406px}
.concept--wild .scroll-cue{left:290px;top:433px}

/* tour cards */
.tour-card{position:absolute;width:124px;height:240px;border-radius:24px;overflow:hidden;color:var(--white);
  box-shadow:0 3px 8px rgba(0,0,0,.25)}
.tour-card .photo{position:absolute;inset:0}
.tour-card .info{position:absolute;left:8px;right:8px;bottom:6px}
.tour-card h3{font-size:10.5px;line-height:13px;font-weight:700;letter-spacing:.5px;margin-bottom:3px}
.tour-card ul{list-style:none;font-size:7px;line-height:12.7px;letter-spacing:.3px}
.tour-card li{display:flex;align-items:center;gap:4px}
.tour-card li::before{content:"";width:5px;height:5px;border-radius:1px;background:var(--white)}
.tour-card li.people::before{border-radius:50% 50% 1px 1px}
.tour-card .price{text-align:right;font-size:15px;font-weight:700;margin-top:6px;letter-spacing:.5px}

.col-1{left:99px}.col-2{left:235px}.col-3{left:371px}
.c1a{top:463px}.c1b{top:722px}.c2a{top:533px}.c2b{top:791px}.c3a{top:497px}.c3b{top:754px}

.t-green .photo{background:linear-gradient(180deg,#4f6b45,#2f3f2c 60%,#1d261b)}
.t-mist .photo{background:linear-gradient(180deg,#888c8f,#6b6f70 50%,#3a3d3c)}
.t-snow .photo{background:linear-gradient(180deg,#6f7880,#a5abb0 45%,#c9cccf)}
.t-palm .photo{background:linear-gradient(180deg,#5a5f63,#7d6d66 55%,#3e3e40)}
.t-giraffe .photo{background:linear-gradient(180deg,#5f7884,#776a55 55%,#3c4539)}
.t-rock .photo{background:linear-gradient(180deg,#3f4448,#7a5a3f 45%,#2a2c2d)}
.t-cat .photo{background:linear-gradient(180deg,#7e6a2c,#4d5a24 50%,#1d2b1a)}
.t-stag .photo{background:linear-gradient(180deg,#3a2e24,#5a3c25 50%,#2a1f18)}
.t-fall .photo{background:linear-gradient(180deg,#5a6266,#7f8a8d 45%,#3a3f40)}
.t-torrent .photo{background:linear-gradient(180deg,#485450,#8c9592 45%,#3a3c3a)}
.t-fungus .photo{background:linear-gradient(180deg,#303a2c,#5a4a3a 55%,#2b3325)}
</style>
</head>
<body>

<!-- Concept A -->
<section class="concept concept--adventure" aria-label="Homepage concept: adventure">
  <div class="hero-photo" role="img" aria-label="Jagged mountain range rising above a sea of clouds"></div>
  <div class="forest-photo" role="img" aria-label="Misty pine forest on hills"></div>

  <header class="site-header">
    <div class="brand"><span>verdalumo</span><span class="brand-dot"></span></div>
    <nav class="main-nav"><span class="currency">EUR</span><span>Wellness Retreat</span><span>Our Climate Pledge</span><span>Partners</span></nav>
    <a class="sign-in">Sign In</a>
  </header>

  <div class="filter filter--retreat"><span class="filter-dot"></span>I need a weekend retreat<span class="chev">⌄</span></div>
  <div class="filter filter--country"><span class="filter-dot"></span>Countries<span class="chev">⌄</span></div>

  <div class="social" aria-label="Social links"><span></span><span></span><span></span><span></span></div>

  <h1 class="headline"><span class="lead">are you ready for an</span><span class="big">ADVENTURE?</span></h1>

  <a class="vote vote--up" aria-label="Thumbs up"><svg viewBox="0 0 24 24"><path fill="#fff" d="M2 10h4v11H2zM8 21V10l5-8c1.6 0 2.5 1 2.2 2.6L14.5 9H21c1.1 0 2 1 1.8 2.1l-1.6 8.2c-.2 1-1 1.7-2 1.7z"/></svg></a>
  <a class="vote vote--reset" aria-label="Reset"><svg viewBox="0 0 24 24"><path fill="none" stroke="#fff" stroke-width="2.6" stroke-linecap="round" d="M6.5 8A7.5 7.5 0 1 1 5 13"/><path fill="#fff" d="M3 4l7 1-4.5 5z"/></svg></a>
  <a class="vote vote--down" aria-label="Thumbs down"><svg viewBox="0 0 24 24"><path fill="#fff" d="M2 3h4v11H2zM8 3v11l5 8c1.6 0 2.5-1 2.2-2.6L14.5 15H21c1.1 0 2-1 1.8-2.1l-1.6-8.2c-.2-1-1-1.7-2-1.7z"/></svg></a>

  <svg class="scroll-cue" viewBox="0 0 12 14"><path fill="none" stroke="#1e1e1e" stroke-width="2" d="M1 1l5 5 5-5M1 7l5 5 5-5"/></svg>

  <div class="sort-by"><span class="funnel"></span>Sort By<span class="chev">⌄</span></div>

  <article class="tour-card t-green col-1 c1a"><div class="photo" role="img" aria-label="Waterfall in a rainforest"></div><div class="info"><h3>2 Days Waterfall Package with BBQ, NSW, Australia</h3><ul><li>2 days / 2 nights</li><li class="people">Minimum no. of persons: 2</li><li class="people">Maximum group size: 4</li><li class="people">Minimum age: 18 years</li></ul><p class="price">$400.00</p></div></article>
  <article class="tour-card t-palm col-1 c1b"><div class="photo" role="img" aria-label="Leaning palm tree by the sea"></div><div class="info"><h3>5 Days Seaside Experience In Mulla Creek, NSW, Australia</h3><ul><li>3 days / 2 nights</li><li class="people">Minimum no. of persons: 1</li><li class="people">Maximum group size: 8</li><li class="people">Minimum age: 10 years</li></ul><p class="price">$190.00</p></div></article>
  <article class="tour-card t-mist col-2 c2a"><div class="photo" role="img" aria-label="Hiker on a misty rock ledge"></div><div class="info"><h3>3 Days Mountain Trekking, Dandenong South, Tanzania</h3><ul><li>3 days / 2 nights</li><li class="people">Minimum no. of persons: 4</li><li class="people">Maximum group size: 10</li><li class="people">Minimum age: 18 years</li></ul><p class="price">$300.00</p></div></article>
  <article class="tour-card t-giraffe col-2 c2b"><div class="photo" role="img" aria-label="Giraffe against the sky"></div><div class="info"><h3>3 Days Big Five Tented Safari, Kruger National Park, South Africa</h3><ul><li>3 days / 2 nights</li><li class="people">Minimum no. of persons: 1</li><li class="people">Maximum group size: 8</li><li class="people">Minimum age: 10 years</li></ul><p class="price">$420.00</p></div></article>
  <article class="tour-card t-snow col-3 c3a"><div class="photo" role="img" aria-label="Climbers crossing a snowfield below peaks"></div><div class="info"><h3>4 Days Snow Climbing, Mount Everest, Himalayas</h3><ul><li>4 days / 3 nights</li><li class="people">Minimum no. of persons: 1</li><li class="people">Maximum group size: 8</li><li class="people">Minimum age: 10 years</li></ul><p class="price">$420.00</p></div></article>
  <article class="tour-card t-rock col-3 c3b"><div class="photo" role="img" aria-label="Tall rock tower above a forest"></div><div class="info"><h3>4 Days Masai Mara And Lake Nakuru Safari Tour In Kenya</h3><ul><li>3 days / 2 nights</li><li class="people">Minimum no. of persons: 1</li><li class="people">Maximum group size: 8</li><li class="people">Minimum age: 10 years</li></ul><p class="price">$280.00</p></div></article>
</section>

<!-- Concept B -->
<section class="concept concept--wild" aria-label="Homepage concept: wild">
  <div class="hero-photo" role="img" aria-label="Red deer stag standing in tall golden grass by a forest edge"></div>
  <div class="forest-photo" role="img" aria-label="Misty pine forest on hills"></div>

  <header class="site-header">
    <div class="brand"><span>verdalumo</span><span class="brand-dot"></span></div>
    <nav class="main-nav"><span class="currency">EUR</span><span>Wellness Retreat</span><span>Our Climate Pledge</span><span>Partners</span></nav>
    <a class="sign-in">Sign In</a>
  </header>

  <div class="social" aria-label="Social links"><span></span><span></span><span></span><span></span></div>

  <div class="filter filter--retreat"><span class="filter-dot"></span>I need a weekend retreat<span class="chev">⌄</span></div>
  <div class="filter filter--country"><span class="filter-dot"></span>Countries<span class="chev">⌄</span></div>

  <h1 class="headline"><span class="lead">step in to the</span><span class="big">WILD?</span></h1>

  <a class="vote vote--up" aria-label="Thumbs up"><svg viewBox="0 0 24 24"><path fill="#fff" d="M2 10h4v11H2zM8 21V10l5-8c1.6 0 2.5 1 2.2 2.6L14.5 9H21c1.1 0 2 1 1.8 2.1l-1.6 8.2c-.2 1-1 1.7-2 1.7z"/></svg></a>
  <a class="vote vote--reset" aria-label="Reset"><svg viewBox="0 0 24 24"><path fill="none" stroke="#fff" stroke-width="2.6" stroke-linecap="round" d="M6.5 8A7.5 7.5 0 1 1 5 13"/><path fill="#fff" d="M3 4l7 1-4.5 5z"/></svg></a>
  <a class="vote vote--down" aria-label="Thumbs down"><svg viewBox="0 0 24 24"><path fill="#fff" d="M2 3h4v11H2zM8 3v11l5 8c1.6 0 2.5-1 2.2-2.6L14.5 15H21c1.1 0 2-1 1.8-2.1l-1.6-8.2c-.2-1-1-1.7-2-1.7z"/></svg></a>

  <svg class="scroll-cue" viewBox="0 0 12 14"><path fill="none" stroke="#1e1e1e" stroke-width="2" d="M1 1l5 5 5-5M1 7l5 5 5-5"/></svg>

  <div class="sort-by"><span class="funnel"></span>Sort By<span class="chev">⌄</span></div>

  <article class="tour-card t-cat col-1 c1a"><div class="photo" role="img" aria-label="Close view of a big cat's fur in green light"></div><div class="info"><h3>2 Days Waterfall Package with BBQ, NSW, Australia</h3><ul><li>2 days / 2 nights</li><li class="people">Minimum no. of persons: 2</li><li class="people">Maximum group size: 4</li><li class="people">Minimum age: 18 years</li></ul><p class="price">$400.00</p></div></article>
  <article class="tour-card t-torrent col-1 c1b"><div class="photo" role="img" aria-label="Rushing water between dark cliffs"></div><div class="info"><h3>5 Days Seaside Experience In Mulla Creek, NSW, Australia</h3><ul><li>3 days / 2 nights</li><li class="people">Minimum no. of persons: 1</li><li class="people">Maximum group size: 8</li><li class="people">Minimum age: 10 years</li></ul><p class="price">$190.00</p></div></article>
  <article class="tour-card t-stag col-2 c2a"><div class="photo" role="img" aria-label="Antlered deer in dark woodland"></div><div class="info"><h3>3 Days Mountain Trekking, Dandenong South, Tanzania</h3><ul><li>3 days / 2 nights</li><li class="people">Minimum no. of persons: 4</li><li class="people">Maximum group size: 10</li><li class="people">Minimum age: 18 years</li></ul><p class="price">$300.00</p></div></article>
  <article class="tour-card t-giraffe col-2 c2b"><div class="photo" role="img" aria-label="Giraffe against the sky"></div><div class="info"><h3>3 Days Big Five Tented Safari, Kruger National Park, South Africa</h3><ul><li>3 days / 2 nights</li><li class="people">Minimum no. of persons: 1</li><li class="people">Maximum group size: 8</li><li class="people">Minimum age: 10 years</li></ul><p class="price">$420.00</p></div></article>
  <article class="tour-card t-fall col-3 c3a"><div class="photo" role="img" aria-label="Tall waterfall in a rocky gorge"></div><div class="info"><h3>4 Days Snow Climbing, Mount Everest, Himalayas</h3><ul><li>4 days / 3 nights</li><li class="people">Minimum no. of persons: 1</li><li class="people">Maximum group size: 8</li><li class="people">Minimum age: 10 years</li></ul><p class="price">$420.00</p></div></article>
  <article class="tour-card t-fungus col-3 c3b"><div class="photo" role="img" aria-label="Red spotted mushroom on a forest floor"></div><div class="info"><h3>4 Days Masai Mara And Lake Nakuru Safari Tour In Kenya</h3><ul><li>3 days / 2 nights</li><li class="people">Minimum no. of persons: 1</li><li class="people">Maximum group size: 8</li><li class="people">Minimum age: 10 years</li></ul><p class="price">$280.00</p></div></article>
</section>

</body>
</html>
```